Banner Ad Design Project

I require banner ad designs with the below wording.

1. Join Today and Make Money Tomorrow. Unlimited Income. Click Here Now

2. I lost my job. Now I Make Over $5,000 Per Week From Home. You Can Too. Free Info, Apply Now

I require sizes: 300x250 and 728x90 and 468x60 and 120x240

The design should communicate legitimate, accredited, online business.

Industry/Entity Type

Business

Requirements
Should not have
• Creative attributes to avoid*
Phone numbers in creative
Creative with no click buttons
Interactive creative
Brand messaging with no call to action
Creative with long looping times

```html
<!DOCTYPE html>
<html lang="en">
<head>
<meta charset="utf-8">
<title>Home Business Banner Set</title>
<link href="https://fonts.googleapis.com/css2?family=Open+Sans:ital,wght@0,400;0,600;0,700;1,600;1,700&display=swap" rel="stylesheet">
<style>
  :root {
    --page: #474f59;
    --sky-deep: #8fd0df;
    --sky-mid: #b9e3ec;
    --sky-light: #e3f4f8;
    --white: #ffffff;
    --ink: #2a3a44;
    --crimson: #d3124a;
    --button-rim: #9aa7ae;
    --url-ink: #4c5a62;
    --photo-top: #e9edf0;
    --photo-bottom: #e6dccb;
  }
  * { margin: 0; padding: 0; box-sizing: border-box; }
  html, body {
    width: 1200px; height: 880px; overflow: hidden;
    background: var(--page);
    font-family: "Open Sans", Arial, sans-serif;
  }
  .sheet {
    position: absolute; left: 0; top: 0;
    width: 800px; height: 587px;
    transform: scale(1.5); transform-origin: 0 0;
  }
  .banner {
    position: absolute; overflow: hidden;
    background: linear-gradient(120deg, var(--sky-deep) 0%, var(--sky-mid) 45%, var(--sky-light) 80%, var(--white) 100%);
  }
  .banner .swoosh { position: absolute; inset: 0; width: 100%; height: 100%; }
  .banner > *:not(.swoosh) { position: absolute; }
  .headline { color: var(--ink); font-weight: 600; letter-spacing: -0.2px; white-space: nowrap; }
  .accent { color: var(--crimson); font-weight: 700; }
  .tagline { color: var(--crimson); font-style: italic; font-weight: 600; white-space: nowrap; }
  .cta {
    display: flex; align-items: center; justify-content: center;
    background: var(--crimson); color: var(--white); font-weight: 600;
    border: 3px solid var(--button-rim); border-radius: 999px; white-space: nowrap;
  }
  .url {
    color: var(--url-ink); font-size: 10.5px; font-weight: 600;
    background: var(--white); border-radius: 999px; padding: 2px 10px;
  }
  .photo {
    border-radius: 4px;
    background: linear-gradient(180deg, var(--photo-top) 0%, var(--photo-bottom) 100%);
  }

  /* 300x250 */
  .rect-join { left: 21px; top: 19px; width: 300px; height: 250px; }
  .rect-join .headline { left: 21px; top: 16px; font-size: 24px; line-height: 28px; }
  .rect-join .tagline { left: 22px; top: 105px; font-size: 19px; line-height: 24px; }
  .rect-join .photo { left: 122px; top: 50px; width: 178px; height: 200px; }
  .rect-join .cta { left: 17px; top: 178px; width: 120px; height: 36px; font-size: 16px; }
  .rect-join .url { left: 0; bottom: 2px; padding-left: 10px; }

  .rect-story { left: 340px; top: 19px; width: 300px; height: 250px; }
  .rect-story .headline { left: 19px; top: 12px; font-size: 18px; line-height: 24px; }
  .rect-story .headline .accent { font-size: 26px; line-height: 34px; }
  .rect-story .tagline { left: 19px; top: 147px; font-size: 16px; }
  .rect-story .photo { left: 122px; top: 50px; width: 178px; height: 200px; }
  .rect-story .cta { left: 17px; top: 178px; width: 120px; height: 36px; font-size: 16px; }
  .rect-story .url { left: 0; bottom: 2px; padding-left: 10px; }

  /* 120x240 */
  .sky-join { left: 659px; top: 19px; width: 120px; height: 245px; }
  .sky-join .headline { left: 9px; top: 12px; font-size: 18.5px; line-height: 20px; }
  .sky-join .tagline { left: 9px; top: 96px; font-size: 12px; }
  .sky-join .photo { left: 16px; top: 118px; width: 90px; height: 92px; }
  .sky-join .cta { left: 13px; top: 214px; width: 93px; height: 28px; font-size: 12.5px; border-width: 2px; }

  /* 728x90 */
  .leader-join { left: 21px; top: 289px; width: 728px; height: 90px; }
  .leader-story { left: 21px; top: 398px; width: 728px; height: 90px; }
  .leader-join .headline { left: 20px; top: 14px; font-size: 24px; }
  .leader-join .tagline { left: 21px; top: 51px; font-size: 18px; }
  .leader-story .headline { left: 20px; top: 8px; font-size: 18px; }
  .leader-story .headline .accent { font-size: 25px; margin-left: 6px; }
  .leader-story .line-two { left: 20px; top: 39px; font-size: 16px; }
  .leader-story .line-two .tagline { position: static; margin-left: 4px; }
  .leader-join .url, .leader-story .url { left: 313px; top: 62px; }
  .leader-join .photo, .leader-story .photo { left: 503px; top: 2px; width: 84px; height: 88px; }
  .leader-join .cta, .leader-story .cta { left: 597px; top: 27px; width: 120px; height: 38px; font-size: 16px; }

  /* 468x60 */
  .strip-join { left: 21px; top: 508px; width: 468px; height: 60px; }
  .strip-join .headline { left: 10px; top: 9px; font-size: 16px; }
  .strip-join .tagline { left: 10px; top: 35px; font-size: 13px; }
  .strip-join .photo { left: 302px; top: 2px; width: 55px; height: 58px; }
  .strip-join .cta { left: 369px; top: 16px; width: 93px; height: 31px; font-size: 13.5px; border-width: 2px; }
</style>
</head>
<body>
<main class="sheet">

  <section class="banner rect-join">
    <svg class="swoosh" viewBox="0 0 300 250" preserveAspectRatio="none" aria-hidden="true"><path d="M0 205 C90 175 200 170 300 185 L300 250 L0 250 Z" fill="#fff"/><path d="M160 0 C230 60 260 120 300 140 L300 0 Z" fill="#fff" opacity=".25"/></svg>
    <div class="photo" role="img" aria-label="Photo of a smiling woman pointing down at a laptop with a seedling growing from a pile of coins"></div>
    <h2 class="headline">Join Today and<br>Make Money<br>Tomorrow</h2>
    <p class="tagline">Unlimited<br>Income</p>
    <a class="cta">Click Here</a>
    <span class="url">www.steady-home-venture.com</span>
  </section>

  <section class="banner rect-story">
    <svg class="swoosh" viewBox="0 0 300 250" preserveAspectRatio="none" aria-hidden="true"><path d="M0 205 C90 175 200 170 300 185 L300 250 L0 250 Z" fill="#fff"/><path d="M160 0 C230 60 260 120 300 140 L300 0 Z" fill="#fff" opacity=".25"/></svg>
    <div class="photo" role="img" aria-label="Photo of a smiling woman pointing down at a laptop with a seedling growing from a pile of coins"></div>
    <h2 class="headline">I lost my job.<br>Now I Make Over<br><span class="accent">$5,000/week</span><br>From Home.<br>You Can Too.</h2>
    <p class="tagline">Free Info</p>
    <a class="cta">Apply Now</a>
    <span class="url">www.steady-home-venture.com</span>
  </section>

  <section class="banner sky-join">
    <svg class="swoosh" viewBox="0 0 120 245" preserveAspectRatio="none" aria-hidden="true"><path d="M0 185 C40 170 80 170 120 180 L120 245 L0 245 Z" fill="#fff"/></svg>
    <div class="photo" role="img" aria-label="Photo of a smiling woman pointing down at a laptop with coins"></div>
    <h2 class="headline">Join Today<br>and Make<br>Money<br>Tomorrow</h2>
    <p class="tagline">Unlimited Income</p>
    <a class="cta">Click Here</a>
  </section>

  <section class="banner leader-join">
    <svg class="swoosh" viewBox="0 0 728 90" preserveAspectRatio="none" aria-hidden="true"><path d="M560 0 C590 30 600 70 580 90 L728 90 L728 0 Z" fill="#fff"/></svg>
    <h2 class="headline">Join Today and Make Money Tomorrow</h2>
    <p class="tagline">Unlimited Income</p>
    <span class="url">www.steady-home-venture.com</span>
    <div class="photo" role="img" aria-label="Photo of a smiling woman pointing down at a laptop with coins"></div>
    <a class="cta">Click Here</a>
  </section>

  <section class="banner leader-story">
    <svg class="swoosh" viewBox="0 0 728 90" preserveAspectRatio="none" aria-hidden="true"><path d="M560 0 C590 30 600 70 580 90 L728 90 L728 0 Z" fill="#fff"/></svg>
    <h2 class="headline">I lost my job. Now I Make Over<span class="accent">$5,000/Week</span></h2>
    <p class="headline line-two">From Home. You Can Too.<span class="tagline">Free Info</span></p>
    <span class="url">www.steady-home-venture.com</span>
    <div class="photo" role="img" aria-label="Photo of a smiling woman pointing down at a laptop with coins"></div>
    <a class="cta">Apply Now</a>
  </section>

  <section class="banner strip-join">
    <svg class="swoosh" viewBox="0 0 468 60" preserveAspectRatio="none" aria-hidden="true"><path d="M350 0 C370 20 375 45 360 60 L468 60 L468 0 Z" fill="#fff"/></svg>
    <h2 class="headline">Join Today &amp; Make Money Tomorrow</h2>
    <p class="tagline">Unlimited Income</p>
    <div class="photo" role="img" aria-label="Photo of a smiling woman pointing down at a laptop with coins"></div>
    <a class="cta">Click Here</a>
  </section>

</main>
</body>
</html>
```